QuillMark Business Cards

I need a business card designed for QuillMark. To get an idea of what we do please visit https://formvault.example/para-creadores-3

```html
<!DOCTYPE html>
<html lang="en">
<head>
<meta charset="utf-8">
<title>QuillMark Business Cards</title>
<link rel="stylesheet" href="https://fonts.googleapis.com/css2?family=Montserrat:wght@400&family=Open+Sans:wght@400;700&display=swap">
<style>
  :root {
    --backdrop: #3a3b3d;
    --card: #1b1f24;
    --card-shade: #21262c;
    --accent: #e8941a;
    --ink-light: #ffffff;
    --rule: #cfd2d6;
  }
  * { box-sizing: border-box; margin: 0; padding: 0; }
  html, body { width: 1200px; height: 1024px; overflow: hidden; }
  body {
    background: var(--backdrop);
    font-family: "Open Sans", Arial, sans-serif;
    position: relative;
  }
  .card {
    position: absolute;
    left: 250px;
    width: 700px;
    height: 400px;
    background: var(--card);
    overflow: hidden;
    box-shadow: 0 14px 30px rgba(0,0,0,0.45);
  }
  .card--front { top: 70px; }
  .card--back { top: 550px; }

  .brand { position: absolute; }
  .brand__name {
    font-family: "Montserrat", Arial, sans-serif;
    font-weight: 400;
    color: var(--ink-light);
    text-transform: uppercase;
    letter-spacing: 0.42em;
    white-space: nowrap;
  }
  .brand__rule {
    height: 1px;
    background: var(--rule);
  }
  .brand__tagline {
    font-family: "Montserrat", Arial, sans-serif;
    color: var(--accent);
    text-transform: uppercase;
    letter-spacing: 0.5em;
    white-space: nowrap;
  }

  /* front */
  .front__block {
    position: absolute;
    left: 50px; top: 70px;
    width: 260px; height: 260px;
    border: 14px solid var(--accent);
  }
  .front__brand { left: 350px; top: 160px; }
  .front__brand .brand__name { font-size: 34px; }
  .front__brand .brand__rule { width: 300px; margin: 10px 0 8px; }
  .front__brand .brand__tagline { font-size: 10px; }

  /* back */
  .back__mark {
    position: absolute;
    left: 44px; top: 46px;
    width: 46px; height: 46px;
    border: 2px solid var(--accent);
  }
  .back__brand { left: 108px; top: 50px; }
  .back__brand .brand__name { font-size: 22px; }
  .back__brand .brand__rule { width: 200px; margin: 6px 0 5px; }
  .back__brand .brand__tagline { font-size: 7px; }

  .back__watermark {
    position: absolute;
    right: 40px; top: 40px;
    width: 260px; height: 260px;
    border: 14px solid var(--card-shade);
  }

  .person { position: absolute; left: 50px; top: 236px; }
  .person__name {
    font-weight: 700;
    font-size: 26px;
    color: var(--accent);
    text-transform: uppercase;
    letter-spacing: 0.02em;
  }
  .person__role {
    font-size: 13px;
    color: var(--ink-light);
    margin-bottom: 12px;
  }
  .contact { list-style: none; }
  .contact__item {
    display: flex;
    align-items: center;
    gap: 8px;
    font-size: 15px;
    color: var(--ink-light);
    line-height: 24px;
  }
  .contact__icon { width: 14px; height: 14px; flex: none; }
</style>
</head>
<body>

<section class="card card--front">
  <div class="front__block"></div>
  <div class="brand front__brand">
    <div class="brand__name">QuillMark</div>
    <div class="brand__rule"></div>
    <div class="brand__tagline">Digital Notary</div>
  </div>
</section>

<section class="card card--back">
  <div class="back__watermark"></div>
  <div class="back__mark"></div>
  <div class="brand back__brand">
    <div class="brand__name">QuillMark</div>
    <div class="brand__rule"></div>
    <div class="brand__tagline">Digital Notary</div>
  </div>

  <div class="person">
    <div class="person__name">Dana Whitfield</div>
    <div class="person__role">Executive Manager</div>
    <ul class="contact">
      <li class="contact__item">
        <svg class="contact__icon" viewBox="0 0 14 14" aria-hidden="true">
          <circle cx="7" cy="7" r="7" fill="var(--accent)"/>
          <path d="M4.3 3.6c.4-.3.8-.2 1 .2l.6 1.1c.2.4.1.7-.2.9l-.4.3c.4.9 1.1 1.6 2 2l.3-.4c.2-.3.5-.4.9-.2l1.1.6c.4.2.5.6.2 1-.5.8-1.3 1-2.2.6-1.7-.7-3-2-3.7-3.7-.4-.9-.2-1.7.4-2.4z" fill="var(--card)"/>
        </svg>
        555-010-0199
      </li>
      <li class="contact__item">
        <svg class="contact__icon" viewBox="0 0 14 14" aria-hidden="true">
          <circle cx="7" cy="7" r="7" fill="var(--accent)"/>
          <rect x="3.5" y="4.5" width="7" height="5" fill="none" stroke="var(--card)" stroke-width="1"/>
          <path d="M3.5 4.8 7 7.4l3.5-2.6" fill="none" stroke="var(--card)" stroke-width="1"/>
        </svg>
        info@quillmark.example
      </li>
      <li class="contact__item">
        <svg class="contact__icon" viewBox="0 0 14 14" aria-hidden="true">
          <circle cx="7" cy="7" r="6.3" fill="none" stroke="var(--accent)" stroke-width="1.2"/>
          <ellipse cx="7" cy="7" rx="2.6" ry="6.3" fill="none" stroke="var(--accent)" stroke-width="1"/>
          <path d="M0.8 7h12.4M2 4h10M2 10h10" stroke="var(--accent)" stroke-width="1"/>
        </svg>
        www.quillmark.example
      </li>
    </ul>
  </div>
</section>

</body>
</html>
```